Harlow Mailbox Services, full-service collaboration with postal service - installation of units

1. CBU - Harlow Mailbox Services - These are Mailbox units that you would see at residential neighborhoods, and Apartments -
2. Logo Needed
3. Maybe have CBU as a division of DWFS (Dermot Vance Field Services)
4. Card to be primary Harlow Mailbox Services

This is a letter of introduction that I am developing:

I am writing to introduce Dermot Vance Field Services, a company dedicated to delivering exceptional service and quality in the installation and maintenance of commercial mailboxes, specifically Cluster Box Units (CBUs). Our commitment to excellence and customer satisfaction has established us as a trusted partner for developers and postal services alike.
At Dermot Vance Field Services, we take pride in our comprehensive approach, ensuring that every step of the mailbox installation process is handled with precision and care. Our services include:
• Supplying high-quality CBUs tailored to meet the specific needs of your development.
• Providing a CBU plat layout upon approval of the address plat, ensuring seamless integration into your development plans.
• Collaborating with developers and postmasters to determine the optimal CBU locations for efficient mail delivery.
• Qualifying the labeling of CBU units, offering both sticker and etching options to suit your preferences.
• Pouring durable concrete foundations as required for the secure installation of the CBU units.
• Handling the installation process with expertise and attention to detail.
• Labeling the units and supplying keys for each mailbox, ensuring a smooth transition for residents and businesses.
Our team is dedicated to working closely with you to ensure that all requirements are met and that the installation process is completed efficiently and to the highest standards.
We look forward to the opportunity to collaborate with you and contribute to the success of your project. Please do not hesitate to contact us for any additional information or to discuss your specific requirements.
Sincerely,
Dermot Vance
Dermot Vance Field Services

Target Market(s)

Developers, Builders, Apartment's, HOA

Industry/Entity Type

Construction

Contact Information for Business Card

Name: Dermot Vance, Cell:555-671-0148, Email: derm@dvfieldco.example

Font styles to use
Serif

Requirements
Must have
• Fresh Looking
Nice to have
• Maybe a CBU Box if it looks clean
Should not have
• Not Industrial or Old traditional card

```html
<!DOCTYPE html>
<html lang="en">
<head>
<meta charset="utf-8">
<title>Harlow Mailbox Services – Business Card</title>
<link href="https://fonts.googleapis.com/css2?family=Montserrat:wght@400;500;700&family=Lato:ital,wght@0,400;1,400&display=swap" rel="stylesheet">
<style>
  :root {
    --stage: #2b2c2e;
    --card-dark: #242426;
    --card-light: #ffffff;
    --ink: #1c1c1c;
    --ink-soft: #5a5a5a;
    --rule: #d9d9d9;
    --brand-gold: #e4a72a;
    --brand-green: #2fa54a;
    --tab: #1e1e1e;
  }
  * { box-sizing: border-box; margin: 0; padding: 0; }
  html, body { width: 1200px; height: 952px; overflow: hidden; }
  body {
    background: var(--stage);
    font-family: "Lato", Arial, sans-serif;
    position: relative;
  }
  .card {
    position: absolute;
    left: 320px;
    width: 560px;
    height: 320px;
    overflow: hidden;
  }
  /* Front */
  .card--front { top: 120px; background: var(--card-dark); }
  .card--front .brand {
    position: absolute;
    inset: 0;
    display: flex; align-items: center; justify-content: center; gap: 22px;
  }
  .brand__mark {
    width: 96px; height: 96px;
    background: var(--brand-gold);
    flex: none;
  }
  .brand__name {
    font-family: "Montserrat", Arial, sans-serif;
    font-weight: 700;
    color: var(--brand-gold);
    font-size: 34px;
    line-height: 1.1;
    text-transform: uppercase;
    letter-spacing: 1px;
  }
  /* Back */
  .card--back { top: 512px; background: var(--card-light); }
  .tab { position: absolute; background: var(--tab); }
  .tab--top { left: 0; top: 46px; width: 12px; height: 70px; }
  .tab--bottom { right: 0; bottom: 42px; width: 12px; height: 70px; }
  .card--back .brand {
    position: absolute;
    left: 46px; top: 76px;
    width: 220px;
    display: flex; align-items: center; gap: 12px;
  }
  .card--back .brand__mark { width: 40px; height: 40px; background: var(--brand-green); }
  .card--back .brand__name {
    font-size: 15px;
    line-height: 1.15;
    letter-spacing: 0.5px;
    color: var(--brand-green);
  }
  .divider {
    position: absolute;
    left: 290px; top: 60px;
    width: 1px; height: 150px;
    background: var(--rule);
  }
  .contact { position: absolute; left: 316px; top: 84px; width: 230px; }
  .contact__name {
    font-family: "Montserrat", Arial, sans-serif;
    font-weight: 700; font-size: 20px; letter-spacing: 1px;
    color: var(--ink);
    white-space: nowrap;
  }
  .contact__role {
    font-family: "Montserrat", Arial, sans-serif;
    font-size: 13px; color: var(--ink-soft); margin: 2px 0 12px;
  }
  .contact__list { list-style: none; }
  .contact__list li {
    display: flex; align-items: center; gap: 8px;
    font-size: 12.5px; color: var(--ink-soft); line-height: 20px;
    white-space: nowrap;
  }
  .contact__list svg { width: 11px; height: 11px; fill: var(--ink); flex: none; }
  .address {
    position: absolute; left: 46px; bottom: 46px;
    font-size: 11.5px; font-style: italic; color: var(--ink-soft);
  }
</style>
</head>
<body>
  <section class="card card--front">
    <div class="brand">
      <span class="brand__mark"></span>
      <span class="brand__name">Harlow<br>Mailbox<br>Services</span>
    </div>
  </section>

  <section class="card card--back">
    <span class="tab tab--top"></span>
    <span class="tab tab--bottom"></span>
    <div class="brand">
      <span class="brand__mark"></span>
      <span class="brand__name">Harlow<br>Mailbox<br>Services</span>
    </div>
    <span class="divider"></span>
    <div class="contact">
      <p class="contact__name">DERMOT VANCE</p>
      <p class="contact__role">Managing Director</p>
      <ul class="contact__list">
        <li><svg viewBox="0 0 24 24"><path d="M6.6 10.8a15 15 0 0 0 6.6 6.6l2.2-2.2a1 1 0 0 1 1-.25 11.4 11.4 0 0 0 3.6.57 1 1 0 0 1 1 1V20a1 1 0 0 1-1 1A17 17 0 0 1 3 4a1 1 0 0 1 1-1h3.5a1 1 0 0 1 1 1c0 1.25.2 2.45.57 3.57a1 1 0 0 1-.25 1z"/></svg>555-671-0148</li>
        <li><svg viewBox="0 0 24 24"><path d="M2 5h20v14H2z M2 5l10 8 10-8"/></svg>derm@dvfieldco.example</li>
        <li><svg viewBox="0 0 24 24"><circle cx="12" cy="12" r="10"/></svg>www.harlowmailbox.example</li>
      </ul>
    </div>
    <p class="address">2170 Linden Park Avenue Washington, DC 20019</p>
  </section>
</body>
</html>
```